Web Design For Metal Recycling Company

We are a scrap and recycling company dealing mainly in scrap metal base in Singapore. We deal in both domestic market and international market. Currently we are still unsure if we want to have a "lively" or "professional" company image so we will leave it to the designer to deem what is good.

We wish for a website to be able to "Retain" the interest of new visitor and at the same time able to give enough information for new and existing customer. We would also wish for design that will get the visitor to "Engage" us.

The attached is the logo for the company and we would want to incorporate that into the website. Either of the logo is fine.

```html
<!DOCTYPE html>
<html lang="en">
<head>
<meta charset="utf-8">
<title>Kim Loh Metals Recycling</title>
<link href="https://fonts.googleapis.com/css2?family=Archivo+Black&family=Cabin:wght@400;600;700&display=swap" rel="stylesheet">
<style>
:root{
  --gold:#d4960a;
  --gold-light:#e2b95d;
  --gold-pale:#f7ead0;
  --yellow:#ffc90e;
  --black:#000;
  --white:#fff;
  --grey:#9a9a9a;
  --field:#e3bb62;
}
*{margin:0;padding:0;box-sizing:border-box}
html,body{width:1200px;height:1137px;overflow:hidden;background:var(--white)}
.page{position:relative;width:1200px;height:1137px;font-family:Arial,Helvetica,sans-serif}
.brand{position:absolute;left:40px;top:19px;display:flex;align-items:center;gap:20px}
.brand-mark{width:54px;height:54px;border:3px solid var(--gold)}
.brand-name{font-family:'Cabin',sans-serif;font-weight:600;color:var(--gold);font-size:22px;line-height:1;letter-spacing:1px}
.call{position:absolute;left:882px;top:0;width:284px;height:60px;background:var(--yellow);border-bottom:2px solid #333;padding:6px 10px}
.call-label{font-family:'Cabin',sans-serif;font-size:14px;color:#222;line-height:1}
.call-number{font-family:'Archivo Black',sans-serif;font-size:22px;color:var(--white);line-height:1.2}
.nav{position:absolute;left:39px;top:111px;width:1127px;height:47px;background:linear-gradient(#f0c84e,var(--gold));border-top:2px solid var(--yellow)}
.nav a{position:absolute;top:12px;font-family:'Cabin',sans-serif;font-size:17px;color:var(--black);text-decoration:none}
.nav a.active{color:var(--white)}
.hero{position:absolute;left:36px;top:181px;width:1130px;height:365px;background:var(--black)}
.hero svg{position:absolute;inset:0;width:100%;height:100%}
.hero-title{position:absolute;left:850px;top:42px;font-family:'Archivo Black',sans-serif;font-size:26px;line-height:36px;color:var(--white);text-shadow:3px 3px 0 var(--black)}
.feature{position:absolute;top:560px;width:360px}
.feature h2{font-family:'Archivo Black',sans-serif;font-size:25px;font-weight:400;color:var(--black);letter-spacing:.5px}
.feature p{margin-top:26px;padding-left:2px;font-size:18px;line-height:22px;color:var(--grey)}
.btn{position:absolute;display:flex;align-items:center;justify-content:center;gap:14px;width:128px;height:40px;background:var(--black);color:var(--yellow);font-family:'Cabin',sans-serif;font-weight:700;font-size:17px}
.btn::after{content:"";border-left:8px solid var(--white);border-top:8px solid transparent;border-bottom:8px solid transparent}
.footer{position:absolute;left:36px;top:786px;width:1130px;height:303px;background:linear-gradient(var(--gold-light) 35%,var(--gold));border-top:2px solid var(--yellow)}
.footer h3{position:absolute;top:17px;font-family:'Archivo Black',sans-serif;font-weight:400;font-size:24px;color:var(--white);letter-spacing:2px}
.rule{position:absolute;top:56px;height:1px;background:var(--white)}
.label{position:absolute;font-family:'Cabin',sans-serif;font-weight:600;font-size:17px;color:var(--black)}
.field{position:absolute;background:var(--field)}
.submit{position:absolute;left:639px;top:245px;width:125px;height:34px;background:var(--black);color:var(--gold);font-family:'Cabin',sans-serif;font-weight:700;font-size:17px;display:flex;align-items:center;justify-content:center}
.social{position:absolute;top:193px;width:24px;height:24px;border-radius:50%;background:var(--white)}
.base{position:absolute;left:0;top:1089px;width:1200px;height:48px;background:var(--black)}
</style>
</head>
<body>
<div class="page">
  <div class="brand">
    <div class="brand-mark"></div>
    <div class="brand-name">KIM LOH METALS RECYCLING</div>
  </div>
  <div class="call">
    <div class="call-label">CALL US</div>
    <div class="call-number">1800-555-0142</div>
  </div>
  <nav class="nav">
    <a style="left:17px">HOME</a>
    <a style="left:107px">ABOUT</a>
    <a style="left:208px">RECYCLING TYPES</a>
    <a class="active" style="left:405px">BRANCHES</a>
    <a style="left:539px">CAREERS</a>
    <a style="left:657px">CONTACT US</a>
  </nav>
  <section class="hero">
    <svg viewBox="0 0 934 301" preserveAspectRatio="none" aria-hidden="true">
      <defs>
        <linearGradient id="sheen" x1="0" y1="0" x2="1" y2="0.6">
          <stop offset="0.45" stop-color="#d4960a"/>
          <stop offset="0.7" stop-color="#f7ead0"/>
          <stop offset="1" stop-color="#d4960a"/>
        </linearGradient>
      </defs>
      <polygon points="623,0 934,0 934,301 773,301 537,101" fill="url(#sheen)"/>
    </svg>
    <div class="hero-title">TYPES OF<br>RECYCLING<br>DONE<br>BY US</div>
  </section>
  <article class="feature" style="left:60px">
    <h2>RECYCLING TYPES</h2>
    <p>Here we explain the types of recycling done by the company. Here we explain the types of recycling<br>done by the company.</p>
  </article>
  <article class="feature" style="left:450px">
    <h2>ABOUT</h2>
    <p>Here we explain the types of recycling done by the company. Here we explain the types of recycling<br>done by the company.</p>
  </article>
  <article class="feature" style="left:817px">
    <h2>SERVICES</h2>
    <p>Here we explain the types of recycling done by the company. Here we explain the types of recycling<br>done by the company.</p>
  </article>
  <div class="btn" style="left:63px;top:723px">Read More</div>
  <div class="btn" style="left:451px;top:725px">Read More</div>
  <div class="btn" style="left:818px;top:725px">Read More</div>
  <footer class="footer">
    <h3 style="left:27px">MAIL US</h3>
    <div class="rule" style="left:27px;width:738px"></div>
    <h3 style="left:783px">ON SOCIAL SITES</h3>
    <div class="rule" style="left:783px;width:333px"></div>
    <div class="label" style="left:30px;top:86px">Name</div>
    <div class="field" style="left:29px;top:109px;width:352px;height:38px"></div>
    <div class="label" style="left:32px;top:161px">Email</div>
    <div class="field" style="left:29px;top:183px;width:352px;height:37px"></div>
    <div class="label" style="left:414px;top:86px">Message</div>
    <div class="field" style="left:414px;top:109px;width:350px;height:110px"></div>
    <div class="submit">SUBMIT</div>
    <div class="social" style="left:788px"></div>
    <div class="social" style="left:844px"></div>
    <div class="social" style="left:905px"></div>
  </footer>
  <div class="base"></div>
</div>
</body>
</html>
```